Creative Web Site to Sell Geology Classes for Homeschooling

I am starting a business to sell a variety of geology classes for homeschoolers. I am targeting classes for kids with dyslexia, although others will benefit as well. The classes will be delivered by mail. Each class will have a video, a manual, and rock samples. I need a landing page that I can link over to seven other pages, a page with a template for products, and a template of the pages that will not have products. All should be easy to edit. All pages should display well with handheld devices (phones), as well as desktops.

```html
<!DOCTYPE html>
<html lang="en">
<head>
<meta charset="utf-8">
<title>Stonebrook Academy – Learn Earth Science</title>
<link rel="stylesheet" href="https://fonts.googleapis.com/css2?family=Montserrat:wght@400;600;700;800&family=Open+Sans:wght@400;600;700&display=swap">
<style>
:root{
  --orange:#f4572e;
  --coral:#f76c63;
  --yellow:#f4b824;
  --yellow-soft:#f7c24a;
  --green:#6ad3ae;
  --green-dark:#55c49c;
  --ink:#222222;
  --text:#6b6b6b;
  --line:#e6e6e6;
  --footer:#3f3d4b;
  --white:#ffffff;
}
*{box-sizing:border-box;margin:0;padding:0}
html,body{width:1200px;height:4186px;overflow:hidden}
body{position:relative;background:var(--white);font-family:"Open Sans",Arial,sans-serif;color:var(--text)}
.abs{position:absolute}
h1,h2,h3,.btn,.nav a,.brand{font-family:"Montserrat",Arial,sans-serif}
.btn{position:absolute;display:flex;align-items:center;justify-content:center;background:var(--orange);color:var(--white);font-weight:800;font-size:13px;letter-spacing:.5px;border-radius:4px 14px 4px 14px;text-transform:uppercase}

/* header */
.brand{position:absolute;left:125px;top:26px;display:flex;align-items:center;gap:12px}
.brand-mark{width:84px;height:84px;border-radius:50%;background:var(--orange)}
.brand-name{font-size:27px;font-weight:800;color:var(--orange);line-height:1}
.nav{position:absolute;top:98px;left:556px;display:flex;gap:27px}
.nav a{font-size:13px;color:#444;text-decoration:none;font-weight:600}
.social-links{position:absolute;display:flex;gap:12px;font-family:"Open Sans",Arial,sans-serif;font-weight:700;font-size:12px;color:var(--yellow)}
.info-bar{position:absolute;left:0;top:134px;width:1200px;height:61px;background:var(--coral);color:var(--white);font-size:10px;font-weight:700;display:flex;align-items:center;padding-left:130px;letter-spacing:.2px}

/* hero */
.hero{position:absolute;left:0;top:195px;width:1200px;height:469px;background:linear-gradient(90deg,#c9d2cf 0%,#dfe3df 35%,#b8a894 62%,#8a6b52 78%,#d8d5cf 100%)}
.hero h1{position:absolute;left:0;width:1200px;top:370px;text-align:center;font-size:46px;font-weight:800;color:#f58960;letter-spacing:1px}

/* intro */
.section-title{position:absolute;left:0;width:1200px;text-align:center;font-family:"Montserrat",Arial,sans-serif;font-weight:700;color:var(--ink);text-transform:uppercase}
.lead{position:absolute;text-align:center;font-size:12px;line-height:21px;color:var(--text)}
.feature{position:absolute;top:921px;width:302px;height:279px;border:1px solid var(--line);background:var(--white);text-align:center}
.feature-icon{width:116px;height:116px;border-radius:50%;margin:20px auto 0;display:flex;align-items:center;justify-content:center}
.feature h3{margin-top:22px;font-size:12px;font-weight:800;color:var(--ink)}
.feature .rule{width:44px;height:2px;margin:6px auto 12px}
.feature p{font-size:11px;line-height:19px;padding:0 48px}
.dot{position:absolute;width:16px;height:16px;border-radius:50%;background:var(--yellow);border:3px solid #fde9b3}

/* topics */
.topics-photo{position:absolute;left:125px;top:1405px;width:370px;height:290px;border-radius:26px;border:3px solid var(--orange);background:linear-gradient(135deg,#e7e2dc,#bcb4aa 55%,#8f8579)}
.topics h2{position:absolute;left:555px;top:1428px;font-size:24px;font-weight:700;color:var(--white)}
.topic{position:absolute;display:flex;align-items:center;gap:12px;color:var(--white);font-size:14px;font-weight:600}
.topic svg{flex:none}

/* courses */
.laptop-screen{position:absolute;left:328px;top:1990px;width:534px;height:352px;background:#1e1e1e;border-radius:14px 14px 0 0;padding:22px 24px 18px}
.video{width:100%;height:100%;background:linear-gradient(110deg,#d3d6d8 0%,#eef0ee 40%,#b69b86 65%,#dfe2e4 100%)}
.laptop-base{position:absolute;left:262px;top:2342px;width:666px;height:24px;background:linear-gradient(#d9d9d9,#a9a9a9);border-radius:0 0 60px 60px/0 0 20px 20px}
.arrow-btn{position:absolute;width:48px;height:48px;border-radius:50%;border:2px solid var(--yellow)}
.pager{position:absolute;top:2431px;left:540px;display:flex;gap:8px}
.pager span{width:26px;height:3px;background:#ddd}
.pager span:first-child{background:var(--coral)}

/* case studies */
.case{position:absolute;background:var(--white);box-shadow:0 4px 18px rgba(0,0,0,.06)}
.case-img{position:absolute;left:0;top:0}
.case h3{font-size:14px;font-weight:600;color:var(--ink);line-height:19px}
.case .date{font-size:10px;color:#999;margin-top:6px}
.case .more{font-size:9px;color:var(--orange);margin-top:14px;font-weight:600;text-transform:uppercase}

/* testimonials */
.person{position:absolute;top:3650px;width:240px;text-align:center;color:var(--white)}
.avatar{width:112px;height:112px;border-radius:50%;border:6px solid var(--white);margin:0 auto;background:linear-gradient(160deg,#c8cdd3,#8e96a0)}
.person h3{font-family:"Montserrat",Arial,sans-serif;font-size:11px;font-weight:700;margin-top:26px}
.person p{font-size:9px;line-height:14px;margin-top:6px;padding:0 10px}

/* footer */
.footer-col{position:absolute;top:4036px;font-size:10px;color:#cfcfd6}
.footer-col h4{font-family:"Montserrat",Arial,sans-serif;font-weight:600;font-size:10px;color:#ffffff;text-transform:uppercase;margin-bottom:12px}
.footer-col li{list-style:none;margin-bottom:13px}
</style>
</head>
<body>

<header>
  <div class="brand"><span class="brand-mark"></span><span class="brand-name">STONEBROOK<br>ACADEMY</span></div>
  <a class="btn" style="left:815px;top:25px;width:130px;height:48px">Get Started</a>
  <div class="social-links" style="left:965px;top:40px"><span>Like</span><span>Post</span><span>Pics</span></div>
  <nav class="nav"><a>HOME</a><a>ABOUT</a><a>SERVICES</a><a>CLASSES</a><a>TESTIMONIALS</a><a>CAREERS</a><a>CONTACT</a></nav>
</header>

<div class="info-bar">PREVIEW COURSE, 3.5 HOURS ON DEMAND VIDEO, 7 HRS ON-DEMAND AUDIO, 12 DOWNLOADABLE RESOURCES, FULL LIFETIME ACCESS, ACCESS ON MOBILE AND TV, CERTIFICATE OF COMPLETION</div>

<section class="hero" role="img" aria-label="Photo of a smiling girl at a laptop in a library">
  <h1>LEARN EARTH SCIENCE</h1>
</section>

<section class="intro">
  <h2 class="section-title" style="top:745px;font-size:24px">Introduction to Geological Processes</h2>
  <p class="lead" style="left:200px;top:798px;width:800px">Sed ut perspiciatis unde omnis iste natus error sit voluptatem accusantium doloremque laudantium, totam rem aperiam, eaque ipsa quae ab illo inventore veritatis et quasi architecto beatae vitae dicta sunt explicabo. Nemo enim ipsam voluptatem quia voluptas sit aspernatur aut odit aut fugit, sed quia consequuntur magni dolores eos qui ratione voluptatem sequi nesciunt. Neque porro quisquam est, qui dolorem ipsum quia dolor sit amet, consectetur, adipisci velit, sed quia non numquam eius modi tempora sint dolore magnam aliquam quaerat voluptatem.</p>

  <span class="dot" style="left:116px;top:1055px"></span>
  <span class="dot" style="left:1064px;top:1055px"></span>

  <article class="feature" style="left:125px">
    <div class="feature-icon" style="border:2px solid var(--orange)">
      <svg width="86" height="86" viewBox="0 0 86 86"><circle cx="43" cy="43" r="42" fill="#fde3dc"/><rect x="22" y="26" width="42" height="28" rx="3" fill="none" stroke="#f4572e" stroke-width="4"/><path d="M36 62h14M43 54v8" stroke="#f4572e" stroke-width="4"/></svg>
    </div>
    <h3>ACCUSAMUS ET IUSTO</h3><div class="rule" style="background:var(--orange)"></div>
    <p>At vero eos et accusamus et iusto odegio nismos ducimus qui blanditiis praesentium voluptatum deleniece corrupti.</p>
  </article>
  <article class="feature" style="left:448px">
    <div class="feature-icon" style="border:2px solid var(--yellow)">
      <svg width="86" height="86" viewBox="0 0 86 86"><circle cx="43" cy="43" r="42" fill="#fdeec4"/><rect x="25" y="20" width="36" height="46" rx="2" fill="#fff" stroke="#f4b824" stroke-width="3"/><path d="M31 32h24M31 40h24M31 48h14" stroke="#f4b824" stroke-width="3"/><circle cx="54" cy="58" r="7" fill="#f4b824"/></svg>
    </div>
    <h3>ACCUSAMUS ET IUSTO</h3><div class="rule" style="background:var(--yellow)"></div>
    <p>At vero eos et accusamus et iusto odegio nismos ducimus qui blanditiis praesentium voluptatum deleniece corrupti.</p>
  </article>
  <article class="feature" style="left:773px">
    <div class="feature-icon" style="border:2px solid var(--green)">
      <svg width="86" height="86" viewBox="0 0 86 86"><circle cx="43" cy="43" r="42" fill="#d6f4e9"/><rect x="22" y="40" width="10" height="22" fill="#55c49c"/><path d="M35 40l10-16c4 0 6 3 5 7l-2 7h12c3 0 5 3 4 6l-4 14c-1 3-3 4-6 4H35z" fill="#6ad3ae"/></svg>
    </div>
    <h3>ACCUSAMUS ET IUSTO</h3><div class="rule" style="background:var(--green)"></div>
    <p>At vero eos et accusamus et iusto odegio nismos ducimus qui blanditiis praesentium voluptatum deleniece corrupti.</p>
  </article>
</section>

<section class="topics">
  <svg class="abs" style="left:0;top:1270px" width="1200" height="600" viewBox="0 0 1200 600" aria-hidden="true">
    <path d="M0 40 C250 -10 450 90 700 40 S1050 -10 1200 50 V530 C1000 610 800 540 600 560 S200 620 0 560 Z" fill="#f6b92c"/>
    <path d="M0 40 C250 -10 450 90 700 40 S1050 -10 1200 50 V70 C1000 20 850 80 650 70 S250 20 0 70 Z" fill="#f8c957"/>
  </svg>
  <div class="topics-photo" role="img" aria-label="Photo of a boy with headphones using a laptop"></div>
  <h2>TOPICS WE WILL COVER</h2>
  <div class="topic" style="left:555px;top:1490px"><svg width="18" height="18" viewBox="0 0 18 18"><circle cx="9" cy="9" r="8" fill="none" stroke="#fff" stroke-width="1.5"/><path d="M5 9l3 3 5-6" fill="none" stroke="#fff" stroke-width="1.8"/></svg>Identifying rocks</div>
  <div class="topic" style="left:555px;top:1525px"><svg width="18" height="18" viewBox="0 0 18 18"><circle cx="9" cy="9" r="8" fill="none" stroke="#fff" stroke-width="1.5"/><path d="M5 9l3 3 5-6" fill="none" stroke="#fff" stroke-width="1.8"/></svg>The rock cycle</div>
  <div class="topic" style="left:555px;top:1560px"><svg width="18" height="18" viewBox="0 0 18 18"><circle cx="9" cy="9" r="8" fill="none" stroke="#fff" stroke-width="1.5"/><path d="M5 9l3 3 5-6" fill="none" stroke="#fff" stroke-width="1.8"/></svg>Sources of metals</div>
  <div class="topic" style="left:800px;top:1490px"><svg width="18" height="18" viewBox="0 0 18 18"><circle cx="9" cy="9" r="8" fill="none" stroke="#fff" stroke-width="1.5"/><path d="M5 9l3 3 5-6" fill="none" stroke="#fff" stroke-width="1.8"/></svg>Plate tectonics</div>
  <div class="topic" style="left:800px;top:1525px"><svg width="18" height="18" viewBox="0 0 18 18"><circle cx="9" cy="9" r="8" fill="none" stroke="#fff" stroke-width="1.5"/><path d="M5 9l3 3 5-6" fill="none" stroke="#fff" stroke-width="1.8"/></svg>Impacts of Earth's resources</div>
  <div class="topic" style="left:800px;top:1560px"><svg width="18" height="18" viewBox="0 0 18 18"><circle cx="9" cy="9" r="8" fill="none" stroke="#fff" stroke-width="1.5"/><path d="M5 9l3 3 5-6" fill="none" stroke="#fff" stroke-width="1.8"/></svg>Mitigating environmental issues</div>
  <a class="btn" style="left:557px;top:1615px;width:142px;height:50px">Get Started</a>
  <div class="topic" style="left:810px;top:1610px">... &amp; More!</div>
</section>

<section class="courses">
  <h2 class="section-title" style="top:1880px;font-size:24px">Our Courses</h2>
  <p class="lead" style="left:350px;top:1925px;width:500px">Sed ut perspiciatis unde omnis iste natussrat voluptatem accusantium doloremque laudantium, totam rem aperiam, eaque ipsa quae.</p>
  <span class="abs" style="left:290px;top:1963px;width:16px;height:16px;border-radius:50%;border:1px solid #ccc"></span>
  <span class="abs" style="left:925px;top:2220px;width:16px;height:16px;border-radius:50%;border:1px solid #ccc"></span>
  <div class="laptop-screen">
    <div class="video" role="img" aria-label="Video still of a girl reading a tablet on the floor"></div>
  </div>
  <svg class="abs" style="left:578px;top:2150px" width="40" height="40" viewBox="0 0 40 40"><circle cx="20" cy="20" r="19" fill="#f4572e"/><path d="M16 12l12 8-12 8z" fill="#fff"/></svg>
  <div class="laptop-base"></div>
  <div class="arrow-btn" style="left:178px;top:2146px"><svg width="44" height="44" viewBox="0 0 44 44"><path d="M25 14l-8 8 8 8" fill="none" stroke="#f4b824" stroke-width="2.5"/></svg></div>
  <div class="arrow-btn" style="left:974px;top:2146px"><svg width="44" height="44" viewBox="0 0 44 44"><path d="M19 14l8 8-8 8" fill="none" stroke="#f4b824" stroke-width="2.5"/></svg></div>
  <div class="pager"><span></span><span></span><span></span></div>

  <h3 class="section-title" style="top:2487px;font-size:15px;color:var(--orange)">Our Manual</h3>
  <p class="lead" style="left:265px;top:2530px;width:670px">Sed ut perspiciatis unde omnis iste natus error sit voluptatem accusantium doloremque laudantium, totam rem aperiam, eaque ipsa quae ab illo inventore veritatis et quasi architecto beatae vitae dicta sunt explicabo. Nemo enim ipsam voluptatem quia voluptas sit aspernatur aut odit aut fugit, sed quia consequuntur magni dolores eos qui ratione.</p>
  <a class="btn" style="left:523px;top:2631px;width:154px;height:48px">Download Now</a>
</section>

<section class="cases">
  <svg class="abs" style="left:0;top:2760px" width="1200" height="720" viewBox="0 0 1200 720" aria-hidden="true">
    <defs><linearGradient id="caseBg" x1="0" x2="1" y1="0" y2="1"><stop offset="0" stop-color="#fdf0f4"/><stop offset="1" stop-color="#ffffff"/></linearGradient></defs>
    <path d="M0 60 C300 0 700 90 1200 40 V720 H0 Z" fill="url(#caseBg)"/>
  </svg>
  <h2 class="section-title" style="top:2868px;font-size:24px">Case Studies</h2>

  <article class="case" style="left:245px;top:2930px;width:340px;height:363px">
    <div class="case-img" role="img" aria-label="Photo of two children reading together" style="width:340px;height:243px;background:linear-gradient(135deg,#f1e6d3,#d9b88f 55%,#b99574)"></div>
    <div style="position:absolute;left:18px;top:262px;right:18px">
      <h3>At vero eosst accusamus distinctio iusto</h3>
      <p class="date">▦ 25 February, 2019</p><p class="more">View Details</p>
    </div>
  </article>
  <article class="case" style="left:593px;top:2930px;width:362px;height:173px">
    <div class="case-img" role="img" aria-label="Photo of a boy writing at a desk" style="width:162px;height:173px;background:linear-gradient(135deg,#d8d9d6,#9a9c98)"></div>
    <div style="position:absolute;left:180px;top:20px;right:12px">
      <h3>Nam libero tempore, cum soluta nobis estsun optio cumquest</h3>
      <p class="date">▦ 25 February, 2019</p><p class="more">View Details</p>
    </div>
  </article>
  <article class="case" style="left:593px;top:3120px;width:362px;height:173px">
    <div class="case-img" role="img" aria-label="Photo of a child using a tablet" style="width:162px;height:173px;background:linear-gradient(135deg,#cfd8de,#7f8e97)"></div>
    <div style="position:absolute;left:180px;top:20px;right:12px">
      <h3>Nam libero tempore, cum soluta nobis estsun optio cumquest</h3>
      <p class="date">▦ 25 February, 2019</p><p class="more">View Details</p>
    </div>
  </article>
  <a class="btn" style="left:520px;top:3340px;width:140px;height:48px">View All</a>
</section>

<section class="testimonials">
  <svg class="abs" style="left:0;top:3450px" width="1200" height="560" viewBox="0 0 1200 560" aria-hidden="true">
    <path d="M0 40 C300 -10 800 70 1200 20 V560 H0 Z" fill="#6ad3ae"/>
  </svg>
  <h2 class="section-title" style="top:3562px;font-size:24px;color:var(--white)">Testimonials</h2>
  <div class="person" style="left:242px"><div class="avatar" role="img" aria-label="Portrait of a customer"></div><h3>Paul Renner</h3><p>Our son finally enjoys science lessons and asks for new rocks each week.</p></div>
  <div class="person" style="left:480px"><div class="avatar" role="img" aria-label="Portrait of a customer"></div><h3>Lena Hartwell</h3><p>The videos and manual are clear and easy to follow for my daughter.</p></div>
  <div class="person" style="left:720px"><div class="avatar" role="img" aria-label="Portrait of a customer"></div><h3>Owen Marsh</h3><p>Great hands-on samples that made every geology topic simple to learn.</p></div>
</section>

<footer>
  <svg class="abs" style="left:0;top:3880px" width="1200" height="306" viewBox="0 0 1200 306" aria-hidden="true">
    <path d="M0 50 C350 0 800 30 1200 0 V306 H0 Z" fill="#3f3d4b"/>
  </svg>
  <svg class="abs" style="left:1071px;top:3908px" width="44" height="44" viewBox="0 0 44 44"><circle cx="22" cy="22" r="21" fill="#fff"/><path d="M22 30V14M16 20l6-6 6 6" fill="none" stroke="#3f3d4b" stroke-width="2"/></svg>
  <div class="brand" style="top:4008px"><span class="brand-mark" style="width:76px;height:76px"></span><span class="brand-name" style="font-size:24px">STONEBROOK<br>ACADEMY</span></div>
  <p class="abs" style="left:125px;top:4118px;font-size:10px;color:#cfcfd6">© Copyrights 2019. All Rights Reserved.</p>
  <div class="footer-col" style="left:473px"><h4>Quick Links</h4><ul><li>Home</li><li>About Us</li><li>Our Courses</li></ul></div>
  <div class="footer-col" style="left:636px"><h4>Other Links</h4><ul><li>Why Us</li><li>Case Studies</li><li>Contact Us</li></ul></div>
  <div class="footer-col" style="left:795px"><h4>Legal</h4><ul><li>Terms &amp; Conditions</li><li>Privacy Policy</li><li>Disclaimers</li></ul></div>
  <div class="social-links" style="left:963px;top:4056px;gap:8px;font-size:9px;color:var(--orange)"><span>Like</span><span>Post</span><span>Pics</span></div>
</footer>

</body>
</html>
```